Online Course Page

We are building a video based online course page. This project is for only the actual page that the student will watch the videos at. They will watch one vide at a time. Once one video lesson is completed then they can move to the next video lesson. The page will need to show the video player. (Main feature.) The list of lessons in the course. Instructor information. Profile picture and bio of the instructor. A Live chat button that will initiate a chat in real-time with the instructor.

The winning designer will also be asked to to design the dashboard area and other aspects of the user interface as an additional project.

Target Market(s)

Adults

Number of Pages Required

1 page

Colors
9bcb3c

Requirements
Must have
• Our logo is attached. Green and grey are our colors. Should feel modern, clean and be simple to navigate. The site will be responsive so the layout should work well on mobile devices.

```html
<!DOCTYPE html>
<html lang="en">
<head>
<meta charset="utf-8">
<title>LearnHarbor – Updates on Supervision</title>
<link rel="stylesheet" href="https://fonts.googleapis.com/css2?family=Open+Sans:wght@400;600;700;800&family=Roboto:wght@300;400;500&display=swap">
<style>
:root{
  --green:#8dc63f;
  --green-bright:#9bcb3c;
  --dark:#2f3436;
  --header:#3b4245;
  --footer:#3a3f42;
  --page:#f7f7f7;
  --white:#ffffff;
  --row:#ececec;
  --text:#333;
  --muted:#c9cdd0;
  --blue:#2f86b7;
  --star:#f6c400;
}
*{box-sizing:border-box;margin:0;padding:0}
html,body{width:1200px;height:1200px;overflow:hidden}
body{position:relative;background:var(--page);font-family:'Roboto',sans-serif;color:var(--text)}

.topbar{position:absolute;left:0;top:0;width:1200px;height:26px;background:var(--dark);
  display:flex;justify-content:flex-end;align-items:center;padding-right:142px;gap:0;
  font:600 9.5px 'Open Sans',sans-serif;color:#fff}
.topbar a{padding:0 8px;border-left:1px solid #fff;line-height:11px}
.topbar a:first-child{border-left:none}
.topbar a.plain{border-left:none}

.mainnav{position:absolute;left:0;top:26px;width:1200px;height:66px;background:var(--header)}
.brand{position:absolute;left:114px;top:20px;display:flex;align-items:center;gap:7px;
  font:700 17px 'Open Sans',sans-serif;color:#fff}
.brand i{width:16px;height:16px;border-radius:50%;background:var(--green);display:block}
.mainnav nav{position:absolute;right:150px;top:26px;display:flex;gap:26px;align-items:center;
  font:700 11px 'Open Sans',sans-serif;color:#fff}

.player{position:absolute;left:114px;top:117px;width:625px;height:412px;background:#2b2b2b}
.poster{position:absolute;left:0;top:0;width:625px;height:353px;
  background:linear-gradient(90deg,#d6d8da 0%,#c8cbcd 55%,#b8bbbe 100%);overflow:hidden}
.poster .figure{position:absolute;left:250px;top:0;width:250px;height:353px;
  background:linear-gradient(180deg,#c9a27e 0%,#d9a441 45%,#6d8fb8 80%,#c9ccce 100%);opacity:.55;border-radius:120px 120px 0 0}
.poster h2{position:absolute;left:30px;top:16px;font:300 82px 'Roboto',sans-serif;color:var(--blue);letter-spacing:1px}
.poster .sub{position:absolute;left:30px;top:98px;font:300 46px 'Roboto',sans-serif;color:var(--blue)}
.poster .year{position:absolute;left:36px;top:270px;font:300 74px 'Roboto',sans-serif;color:var(--blue)}
.poster .badge{position:absolute;left:496px;top:2px;width:100px;height:100px;border-radius:50%;background:#1f3f73}
.bigplay{position:absolute;left:241px;top:96px}
.controls{position:absolute;left:0;top:353px;width:625px;height:59px;background:#262626}
.controls svg{position:absolute}
.time{position:absolute;left:423px;top:18px;font:500 20px 'Roboto',sans-serif;color:#fff}

.instructor{position:absolute;left:114px;top:562px;width:120px;text-align:center}
.avatar{width:84px;height:84px;border-radius:50%;margin:0 auto;background:linear-gradient(160deg,#2f5a3e,#556b59);border:2px solid #e5e5e5}
.instructor .name{margin-top:12px;font:400 13px/15px 'Roboto',sans-serif;color:#333}
.chat{display:block;position:relative;margin-top:12px;height:24px;background:var(--green);color:#fff;font:400 13px/24px 'Roboto',sans-serif}
.chat::after{content:"";position:absolute;left:90px;bottom:-7px;border-left:10px solid transparent;border-top:8px solid var(--green)}
.bio{position:absolute;left:274px;top:557px;width:468px;font:400 9.3px/21px 'Roboto',sans-serif;color:#444}
.readmore{position:absolute;left:275px;top:655px;font:400 11.5px 'Roboto',sans-serif;color:#333}

.course{position:absolute;left:754px;top:117px;width:304px;height:613px;background:var(--white)}
.progress{height:40px;background:var(--green);padding:9px 38px 0;color:#fff;font:400 10px 'Roboto',sans-serif}
.progress span{margin-right:30px}
.progress .bar{margin-top:5px;height:4px;background:#fff;border-radius:2px;width:228px}
.course .label{margin:10px 0 0;font:400 11.5px 'Roboto',sans-serif;color:#333}
.course h1{margin-top:6px;font:500 12.5px 'Roboto',sans-serif;color:var(--green);letter-spacing:.2px;margin-bottom:8px}
.lesson{height:32px;background:var(--row);display:flex;align-items:center;padding:0 46px 0 43px;justify-content:space-between;font:400 11px 'Roboto',sans-serif;color:#333;position:relative}
.lesson svg{position:absolute;left:14px;top:10px}
.items{padding:13px 0 9px 13px;list-style:none}
.items li{display:flex;align-items:center;gap:10px;height:28px;font:400 12.5px 'Roboto',sans-serif;color:#333}

footer{position:absolute;left:0;top:746px;width:1200px;height:454px;background:var(--footer);color:#fff}
.col{position:absolute;top:31px}
.col h3{font:800 11.5px 'Open Sans',sans-serif;letter-spacing:-.2px;margin-bottom:12px}
.about p{font:400 11.5px/15px 'Open Sans',sans-serif;letter-spacing:-.3px}
.about strong{display:block;margin-top:10px;font:800 11px 'Open Sans',sans-serif}
.card{position:absolute;left:0;display:flex;gap:13px;width:210px}
.thumb{width:36px;height:28px;flex:none;background:linear-gradient(135deg,#7fa0c0,#c9d4de)}
.thumb.warm{background:linear-gradient(135deg,#c8744a,#9fb4c8)}
.thumb.crowd{background:linear-gradient(135deg,#6d6a4f,#b8ad85)}
.thumb.people{background:linear-gradient(135deg,#d9d9d9,#8c8c8c)}
.thumb.red{background:linear-gradient(135deg,#b23b2e,#e0b9a0)}
.card .t{font:400 11.5px/17px 'Open Sans',sans-serif;letter-spacing:-.3px}
.stars{color:var(--star);font-size:13px;letter-spacing:-1px;line-height:16px}
.meta{font:800 8px/13px 'Open Sans',sans-serif;margin-top:3px}
.tabs{width:217px;height:47px;background:#55595c;padding:9px 0 0 0;font:800 10px/14px 'Open Sans',sans-serif}
.tabs b{color:var(--green)}
.group{position:absolute;left:0;display:flex;gap:15px;width:220px}
.gicon{width:34px;height:30px;flex:none;background:#f2f2f2}
.gicon.blue{background:linear-gradient(135deg,#2f5fa0,#8aa0b8)}
.group .n{font:400 12px/17px 'Open Sans',sans-serif;letter-spacing:-.3px}
.group .a{font:400 8.5px 'Open Sans',sans-serif;color:#ddd;margin-top:2px}
.totop{position:absolute;left:1043px;top:410px;width:33px;height:33px;background:#2b2f31;text-align:center;font:700 7px 'Open Sans',sans-serif;padding-top:4px}
</style>
</head>
<body>

<div class="topbar">
  <a>ABOUT</a><a>CONTACT US</a><a>SUPPORT</a><a>CART</a><a class="plain">LOGIN</a><a>SIGN UP</a>
</div>

<header class="mainnav">
  <div class="brand"><i></i>LearnHarbor</div>
  <nav>
    <span>ALL COURSES</span><span>ALL INSTRUCTORS</span><span>ARTICLES</span>
    <svg width="12" height="12" viewBox="0 0 12 12"><circle cx="5" cy="5" r="3.8" fill="none" stroke="#fff" stroke-width="1.8"/><line x1="8" y1="8" x2="11" y2="11" stroke="#fff" stroke-width="2"/></svg>
  </nav>
</header>

<section class="player">
  <div class="poster" role="img" aria-label="Course video thumbnail: a smiling woman seated cross-legged with a laptop against a grey wall">
    <div class="figure"></div>
    <h2>3 HOUR</h2>
    <div class="sub">REFRESHER</div>
    <div class="year">2018</div>
    <div class="badge" role="img" aria-label="Continuing education provider badge"></div>
  </div>
  <svg class="bigplay" width="144" height="144" viewBox="0 0 144 144">
    <circle cx="72" cy="72" r="71" fill="#707070" fill-opacity=".85" stroke="#555" stroke-width="1"/>
    <polygon points="56,48 56,100 100,74" fill="#fff"/>
  </svg>
  <div class="controls">
    <svg style="left:36px;top:17px" width="22" height="26" viewBox="0 0 22 26"><polygon points="2,1 2,25 21,13" fill="#fff"/></svg>
    <svg style="left:91px;top:20px" width="316" height="20" viewBox="0 0 316 20">
      <rect x="1" y="4" width="313" height="12" rx="6" fill="#111" stroke="#333"/>
      <rect x="1" y="4" width="48" height="12" rx="6" fill="var(--green)"/>
      <circle cx="48" cy="10" r="9" fill="#f1f1f1"/>
    </svg>
    <div class="time">0:34</div>
    <svg style="left:498px;top:16px" width="34" height="28" viewBox="0 0 34 28">
      <polygon points="1,9 8,9 16,2 16,26 8,19 1,19" fill="#fff"/>
      <path d="M21 8 Q25 14 21 20" stroke="#fff" stroke-width="2.5" fill="none"/>
      <path d="M26 4 Q32 14 26 24" stroke="#fff" stroke-width="2.5" fill="none"/>
    </svg>
    <svg style="left:564px;top:16px" width="26" height="26" viewBox="0 0 26 26">
      <polygon points="15,1 25,1 25,11" fill="#fff"/><line x1="23" y1="3" x2="16" y2="10" stroke="#fff" stroke-width="2.5"/>
      <polygon points="1,15 1,25 11,25" fill="#fff"/><line x1="3" y1="23" x2="10" y2="16" stroke="#fff" stroke-width="2.5"/>
    </svg>
  </div>
</section>

<aside class="instructor">
  <div class="avatar" role="img" aria-label="Instructor portrait in front of a green chalkboard"></div>
  <div class="name">Dr. Martin R. Ellery<br>BCBA-D</div>
  <a class="chat">Live Chat</a>
</aside>
<p class="bio">Dr. Martin Ellery is a Board Certified and Licensed Behavior Analyst and a Licensed Psychologist. He is Chief Executive Officer of Northfield Behavioral Services, a company which provides in person and on-line consultation and training to educational and service organizations around the world; and an Associate Professor in the College of Education and Human Development at Eastbrook University in Linden, Ohio, USA. Dr.</p>
<a class="readmore">Read more...</a>

<section class="course">
  <div class="progress"><span>COURSE PROGRESS:</span>50%<div class="bar"></div></div>
  <div class="label">COURSE</div>
  <h1>UPDATES ON SUPERVISION</h1>

  <div class="lesson"><svg width="16" height="12" viewBox="0 0 16 12"><polyline points="1,6 6,11 15,1" fill="none" stroke="var(--green)" stroke-width="1.6"/></svg><span>LESSON 1</span><span>2/2</span></div>
  <ul class="items">
    <li><svg width="16" height="16"><circle cx="8" cy="8" r="8" fill="var(--green)"/><polyline points="4,8 7,11 12,5" fill="none" stroke="#fff" stroke-width="1.8"/></svg>Purposes of Supervision</li>
    <li><svg width="16" height="16"><circle cx="8" cy="8" r="8" fill="var(--green)"/><polyline points="4,8 7,11 12,5" fill="none" stroke="#fff" stroke-width="1.8"/></svg>3 Hour Refresher Quiz 1</li>
  </ul>

  <div class="lesson"><span>LESSON 2</span><span>1/2</span></div>
  <ul class="items">
    <li><svg width="16" height="16"><circle cx="8" cy="8" r="8" fill="var(--green)"/><polyline points="4,8 7,11 12,5" fill="none" stroke="#fff" stroke-width="1.8"/></svg>New Requirements</li>
    <li><svg width="16" height="16"><circle cx="8" cy="8" r="7.3" fill="none" stroke="var(--green)" stroke-width="1.2"/><polyline points="4,8 7,11 12,5" fill="none" stroke="var(--green)" stroke-width="1.4"/></svg>3 Hour Refresher Quiz 2</li>
  </ul>

  <div class="lesson"><span>LESSON 3</span><span>0/2</span></div>
  <ul class="items">
    <li><svg width="16" height="16"><circle cx="8" cy="8" r="7.3" fill="none" stroke="var(--green)" stroke-width="1.2"/><polyline points="4,8 7,11 12,5" fill="none" stroke="var(--green)" stroke-width="1.4"/></svg>Keeping Yourself and Your Supervisees Safe</li>
    <li><svg width="16" height="16"><circle cx="8" cy="8" r="7.3" fill="none" stroke="var(--green)" stroke-width="1.2"/><polyline points="4,8 7,11 12,5" fill="none" stroke="var(--green)" stroke-width="1.4"/></svg>3 Hour Refresher Quiz 3</li>
  </ul>

  <div class="lesson"><span>LESSON 4</span><span>0/2</span></div>
  <ul class="items">
    <li><svg width="16" height="16"><circle cx="8" cy="8" r="7.3" fill="none" stroke="var(--green)" stroke-width="1.2"/><polyline points="4,8 7,11 12,5" fill="none" stroke="var(--green)" stroke-width="1.4"/></svg>Smart Supervisees</li>
    <li><svg width="16" height="16"><circle cx="8" cy="8" r="7.3" fill="none" stroke="var(--green)" stroke-width="1.2"/><polyline points="4,8 7,11 12,5" fill="none" stroke="var(--green)" stroke-width="1.4"/></svg>3 Hour Refresher Quiz 4</li>
  </ul>

  <div class="lesson"><span>LESSON 4</span><span>0/2</span></div>
  <ul class="items">
    <li><svg width="16" height="16"><circle cx="8" cy="8" r="7.3" fill="none" stroke="var(--green)" stroke-width="1.2"/><polyline points="4,8 7,11 12,5" fill="none" stroke="var(--green)" stroke-width="1.4"/></svg>Upcoming Changes to Supervision!</li>
    <li><svg width="16" height="16"><circle cx="8" cy="8" r="7.3" fill="none" stroke="var(--green)" stroke-width="1.2"/><polyline points="4,8 7,11 12,5" fill="none" stroke="var(--green)" stroke-width="1.4"/></svg>3 Hour Supervision Quiz 5</li>
  </ul>
</section>

<footer>
  <div class="col about" style="left:118px;width:220px">
    <h3>ABOUT LEARNHARBOR</h3>
    <p>LearnHarbor would like to thank all of our amazing instructors and partners!</p>
    <strong>WE COULDN'T DO IT WITHOUT YOU!</strong>
  </div>

  <div class="col" style="left:358px;width:220px;height:420px">
    <h3>POPULAR COURSES</h3>
    <div class="card" style="top:25px"><div class="thumb" role="img" aria-label="Course thumbnail"></div><div><div class="t">From Workshops to Workplaces: Achieving the Goals of Employment First</div><div class="stars">★★★★☆</div><div class="meta">( 5 REVIEWS )<br>127 STUDENTS</div></div></div>
    <div class="card" style="top:132px"><div class="thumb warm" role="img" aria-label="Course thumbnail"></div><div><div class="t">Financial Literacy: Increasing Your Knowledge to Take Charge of Your Finances</div><div class="stars">★★★★☆</div><div class="meta">( 8 REVIEWS )<br>110 STUDENTS</div></div></div>
    <div class="card" style="top:239px"><div class="thumb crowd" role="img" aria-label="Course thumbnail"></div><div><div class="t">AMT Level One Certification</div><div class="stars">★★★★☆</div><div class="meta">( 1 REVIEWS )<br>37 STUDENTS</div></div></div>
    <div class="card" style="top:311px"><div class="thumb people" role="img" aria-label="Course thumbnail"></div><div><div class="t">Behavior Analysis Supervisor Training 2018 Edition</div><div class="stars">☆☆☆☆☆</div><div class="meta">( 0 REVIEWS )<br>16 STUDENTS</div></div></div>
  </div>

  <div class="col" style="left:599px;width:220px;height:420px">
    <h3>MOST RATED</h3>
    <div class="card" style="top:25px"><div class="thumb warm" role="img" aria-label="Course thumbnail"></div><div><div class="t">Financial Literacy: Increasing Your Knowledge to Take Charge of Your Finances</div><div class="stars">★★★★☆</div><div class="meta">( 8 REVIEWS )<br>110 STUDENTS</div></div></div>
    <div class="card" style="top:132px"><div class="thumb" role="img" aria-label="Course thumbnail"></div><div><div class="t">From Workshops to Workplaces: Achieving the Goals of Employment First</div><div class="stars">★★★★☆</div><div class="meta">( 5 REVIEWS )<br>127 STUDENTS</div></div></div>
    <div class="card" style="top:239px"><div class="thumb crowd" role="img" aria-label="Course thumbnail"></div><div><div class="t">AMT Level One Certification</div><div class="stars">★★★★☆</div><div class="meta">( 1 REVIEWS )<br>37 STUDENTS</div></div></div>
    <div class="card" style="top:311px"><div class="thumb red" role="img" aria-label="Course thumbnail"></div><div><div class="t">Transitioning to the Workplace: A Seat at the Table</div><div class="stars">★★★★☆</div><div class="meta">( 1 REVIEWS )<br>2 STUDENTS</div></div></div>
  </div>

  <div class="col" style="left:839px;width:220px;height:420px">
    <h3 style="font-weight:400">GROUPS</h3>
    <div class="tabs">NEWEST | <b>ACTIVE</b> | POPULAR |<br>ALPHABETICAL</div>
    <div class="group" style="top:90px"><div class="gicon" role="img" aria-label="Group avatar"></div><div><div class="n">Autism Group</div><div class="a">active 2 days, 7 hours ago</div></div></div>
    <div class="group" style="top:146px"><div class="gicon" style="background:#dcdcdc" role="img" aria-label="Group avatar"></div><div><div class="n">Behavior Analysis Supervisor Training</div><div class="a">active 1 week, 5 days ago</div></div></div>
    <div class="group" style="top:218px"><div class="gicon blue" role="img" aria-label="Group avatar"></div><div><div class="n">CPSN</div><div class="a">active 3 months, 4 weeks ago</div></div></div>
  </div>

  <div class="totop"><svg width="12" height="8" viewBox="0 0 12 8"><polyline points="1,7 6,2 11,7" fill="none" stroke="#fff" stroke-width="2"/></svg><br>TOP</div>
</footer>

</body>
</html>
```